Tender / Request for Quotation response template

VELKOR42 is a small consulting company that works in management consulting with a particular emphasis on tourism, sport, major events and general commercial. our clients range from government , councils, private businesses and industry associations.

we are regularly asked to submit detailed quotes or tender responses and we use our own PowerPoint template to do so as we find it its generally easier to work with.

our website provides more detail : www.velkor42.com.au the colour of the blue in logo is #000033

our submissions range from 30 pages to 100 pages depending on the size and scale of the project - so we need flexibility with the templates.

Our submissions generally include cover page and table of contents and then
1. Project overview
2. About VELKOR42
3. The project team including bios
4. Initial Insights
5. importance of sustainability
6. Project methodology - example being
6.1 situation analysis
- research
- consultation and engagement
- relevant audits
- relevant economic analysis including graphs
- gap analysis
- SWOT
6.2 Issues and opportunities
6.3 draft report
6.4 final report
7. Case studies and previous relevant work
8. Project timeline
9. Project budget
10. Insurance and referees

we use many graphs and tables from excel and images generally sourced from the web. we also use icons as appropriate so we need graph templates - column, bar / pie etc and table templates.

the feel is on the formal corporate side given the size and scale of projects and clients but with bright and clear graphics and photos.

i have attached 2 copies of confidential submissions that we have made in recent weeks. one long form and one short form to give you an idea of the flexibility we need in the submission process.

if we are happy with the proposed PowerPoint tender submission template we would then look to have a similar one created to use in the development of the actual reports themselves .

hopefully this provides enough information but if not please reach out for more information

our logo and general format are in the attached examples

Target Market(s)

government, council, corporates and private businesses

Industry/Entity Type

management consulting with emphasis on tourism sport major events nd general commerical

Font styles to use
Other font styles liked:
• we usually use calbiri but open to other standard microsoft off the shelf fonts

Colors
0054AA
0677BA
7BADD7
CADEEF
E8F1F8
0094D4
00A9DD
6FCCEA
C7EBF8
E9F6FB

Requirements
Must have
• page for each of the sections detailed in the project brief. image placement - small and large, table and graph formats,

```html
<!DOCTYPE html>
<html lang="en">
<head>
<meta charset="utf-8">
<title>VELKOR42 Tender Response Template</title>
<link href="https://fonts.googleapis.com/css2?family=Montserrat:wght@400;600;700;800&family=Open+Sans:wght@400;600&display=swap" rel="stylesheet">
<style>
:root{
  --navy:#211f52;
  --navy-deep:#000033;
  --grey:#8f93a3;
  --grey-light:#d9dbe2;
  --line:#e3e4ea;
  --paper:#ffffff;
  --backdrop:#eceef2;
  --text:#5a5d6b;
  --photo-a:#7d8797;
  --photo-b:#c9ced8;
}
*{box-sizing:border-box;margin:0;padding:0}
html,body{width:900px;height:1200px;overflow:hidden;background:var(--backdrop)}
.deck{width:900px;height:1200px;padding:22px 24px;display:grid;grid-template-columns:repeat(3,272px);grid-template-rows:repeat(7,153px);column-gap:18px;row-gap:14px}
.slide{position:relative;background:var(--paper);overflow:hidden;box-shadow:0 1px 3px rgba(0,0,40,.15);font-family:'Open Sans',sans-serif;color:var(--text)}
.slide.dark{background:var(--navy);color:#fff}
.head{position:absolute;top:10px;left:12px;font:700 8.5px 'Montserrat',sans-serif;color:var(--navy)}
.mark{position:absolute;top:8px;right:10px;width:10px;height:10px;background:var(--navy)}
.dark .mark{background:#fff}
.copy{font-size:4.6px;line-height:1.55;color:var(--text)}
.dark .copy{color:#c9cbe0}
.photo{position:absolute;background:linear-gradient(135deg,var(--photo-b),var(--photo-a))}
.brand{display:flex;align-items:center;gap:3px;font:700 6px 'Montserrat',sans-serif;color:var(--navy)}
.brand i{display:block;width:7px;height:7px;border-radius:50%;background:var(--navy)}
.dark .brand{color:#fff}.dark .brand i{background:#fff}
.kicker{font:600 5px 'Montserrat',sans-serif;letter-spacing:.8px;color:var(--grey)}
.big{font:800 13px/1.05 'Montserrat',sans-serif;color:var(--navy);text-transform:uppercase}
.dark .big{color:#fff}
.url{font-size:4.6px;color:var(--navy)}
.dark .url{color:#c9cbe0}
.sub{font:700 5.4px 'Montserrat',sans-serif;color:var(--navy)}
svg{display:block}
/* contents */
.toc{position:absolute;top:30px;left:12px;right:12px;display:grid;grid-template-columns:1fr 1fr;gap:9px 14px}
.toc li{list-style:none;display:flex;gap:5px;align-items:center;border-bottom:1px solid var(--line);padding-bottom:5px}
.toc b{font:800 8px 'Montserrat',sans-serif;color:var(--navy)}
.toc span{font:600 5px 'Montserrat',sans-serif;color:var(--text)}
/* budget table */
.budget{position:absolute;top:28px;left:12px;right:12px;border-collapse:collapse;font-size:4.8px}
.budget th{background:var(--navy);color:#fff;font:600 5px 'Montserrat',sans-serif;padding:4px;text-align:left}
.budget td{padding:4px;border-bottom:1px solid var(--line)}
.budget tr:nth-child(even) td{background:#f3f4f7}
</style>
</head>
<body>
<main class="deck">

<!-- Cover light -->
<section class="slide cover-light">
  <div class="photo" style="left:0;top:0;width:118px;height:153px" role="img" aria-label="Photo of a business team standing together"></div>
  <div style="position:absolute;left:130px;top:22px">
    <div class="brand"><i></i>VELKOR42</div>
    <p class="kicker" style="margin-top:22px">PRESENTATION</p>
    <p class="big" style="margin-top:3px">Business<br>Marketing</p>
    <p class="copy" style="margin-top:6px;width:120px">Tender and quotation response for public and private clients.</p>
    <p class="url" style="margin-top:8px">www.velkor42.com.au</p>
  </div>
</section>

<!-- Cover dark -->
<section class="slide dark cover-dark">
  <div class="photo" style="right:0;top:0;width:140px;height:153px" role="img" aria-label="Photo of consultants working at a laptop"></div>
  <div style="position:absolute;left:12px;top:22px">
    <div class="brand"><i></i>VELKOR42</div>
    <p class="kicker" style="margin-top:22px;color:#b6b8d0">PRESENTATION</p>
    <p class="big" style="margin-top:3px">Business<br>Marketing</p>
    <p class="url" style="margin-top:10px">www.velkor42.com.au</p>
  </div>
</section>

<!-- Contents -->
<section class="slide contents">
  <h2 class="head">Contents</h2><span class="mark"></span>
  <ul class="toc">
    <li><b>01</b><span>Project Overview</span></li>
    <li><b>04</b><span>Initial Insights</span></li>
    <li><b>02</b><span>About VELKOR42</span></li>
    <li><b>05</b><span>Sustainability</span></li>
    <li><b>03</b><span>Project Team</span></li>
    <li><b>06</b><span>Methodology</span></li>
  </ul>
</section>

<!-- Project overview -->
<section class="slide overview">
  <h2 class="head">Project Overview</h2><span class="mark"></span>
  <div class="photo" style="left:12px;top:28px;width:248px;height:58px" role="img" aria-label="Photo of a team meeting in an office"></div>
  <div style="position:absolute;left:12px;right:12px;top:94px;display:grid;grid-template-columns:repeat(3,1fr);gap:8px">
    <p class="copy">Scope, objectives and key deliverables for the client brief.</p>
    <p class="copy">Stakeholders, locations and the context of the project.</p>
    <p class="copy">Expected outcomes and measures of success at completion.</p>
  </div>
</section>

<!-- About -->
<section class="slide about">
  <h2 class="head">About VELKOR42</h2><span class="mark"></span>
  <div style="position:absolute;left:12px;top:30px;width:118px">
    <p class="sub">Management consulting</p>
    <p class="copy" style="margin-top:4px">We advise government, councils, businesses and industry associations across tourism, sport, major events and general commercial projects, delivering clear strategy and practical plans.</p>
  </div>
  <div class="photo" style="right:0;top:26px;width:128px;height:100px" role="img" aria-label="Photo of a consultant presenting to clients"></div>
</section>

<!-- Team -->
<section class="slide team">
  <h2 class="head">The Project Team Including Bios</h2><span class="mark"></span>
  <div class="photo" style="left:12px;top:30px;width:70px;height:90px" role="img" aria-label="Portrait photo of team member"></div>
  <div style="position:absolute;left:92px;top:34px;right:14px">
    <p class="sub" style="font-size:7px">Marek Olund</p>
    <p class="kicker" style="margin-top:2px">PROJECT DIRECTOR</p>
    <p class="copy" style="margin-top:6px">Twenty years leading tourism and major event strategies for state agencies and regional councils, with a focus on economic impact.</p>
  </div>
</section>

<!-- Initial insights -->
<section class="slide insights">
  <h2 class="head">Initial Insights</h2><span class="mark"></span>
  <svg style="position:absolute;left:12px;top:30px" width="248" height="110" viewBox="0 0 248 110" aria-hidden="true">
    <g fill="none" stroke="#211f52" stroke-width="3" stroke-linejoin="round">
      <path d="M20 30 H108 a14 14 0 0 1 0 28 H20 a14 14 0 0 0 0 28 H108"/>
      <path d="M140 30 H228 a14 14 0 0 1 0 28 H140 a14 14 0 0 0 0 28 H228"/>
    </g>
    <g fill="#211f52">
      <circle cx="20" cy="30" r="9"/><circle cx="108" cy="86" r="9"/>
      <circle cx="140" cy="30" r="9"/><circle cx="228" cy="86" r="9"/>
    </g>
  </svg>
  <p class="copy" style="position:absolute;left:46px;top:36px;width:70px">Market trends</p>
  <p class="copy" style="position:absolute;left:44px;top:90px;width:70px">Visitor demand</p>
  <p class="copy" style="position:absolute;left:166px;top:36px;width:70px">Funding options</p>
  <p class="copy" style="position:absolute;left:164px;top:90px;width:70px">Delivery risks</p>
</section>

<!-- Sustainability -->
<section class="slide sustain">
  <h2 class="head">Importance Of Sustainability</h2><span class="mark"></span>
  <div style="position:absolute;left:12px;top:30px;width:110px;height:100px;background:var(--navy);padding:12px 10px">
    <p style="font:700 6.5px/1.35 'Montserrat',sans-serif;color:#fff">WHAT'S A STATEMENT THAT SHOWS THE VALUE OF THE VELKOR42 TEAM?</p>
  </div>
  <p class="copy" style="position:absolute;left:132px;top:34px;right:14px">Environmental, social and economic sustainability guide every recommendation, so projects remain viable long after delivery and benefit the wider community.</p>
</section>

<!-- Methodology divider -->
<section class="slide dark method">
  <span class="mark"></span>
  <div style="position:absolute;left:80px;top:48px;width:112px;height:56px;border:1.5px solid #fff;display:flex;align-items:center;justify-content:center;text-align:center">
    <p style="font:800 9px/1.2 'Montserrat',sans-serif;color:#fff">PROJECT<br>METHODOLOGY</p>
  </div>
</section>

<!-- Situation analysis -->
<section class="slide situation">
  <h2 class="head">Situation Analysis</h2><span class="mark"></span>
  <p class="copy" style="position:absolute;left:12px;top:32px;width:100px">A review of current conditions, policy settings and existing assets frames the starting point for the project.</p>
  <svg style="position:absolute;left:140px;top:26px" width="110" height="110" viewBox="0 0 110 110" aria-hidden="true">
    <g fill="none" stroke-width="22">
      <circle cx="55" cy="55" r="36" stroke="#d9dbe2"/>
      <circle cx="55" cy="55" r="36" stroke="#211f52" stroke-dasharray="100 227" transform="rotate(-90 55 55)"/>
      <circle cx="55" cy="55" r="36" stroke="#8f93a3" stroke-dasharray="60 227" stroke-dashoffset="-104" transform="rotate(-90 55 55)"/>
    </g>
  </svg>
</section>

<!-- Research -->
<section class="slide research">
  <h2 class="head">Research</h2><span class="mark"></span>
  <svg style="position:absolute;left:12px;top:34px" width="150" height="70" viewBox="0 0 150 70" aria-hidden="true">
    <g fill="none" stroke-width="9">
      <circle cx="35" cy="35" r="26" stroke="#d9dbe2"/>
      <circle cx="35" cy="35" r="26" stroke="#211f52" stroke-dasharray="106 164" transform="rotate(-90 35 35)"/>
      <circle cx="110" cy="35" r="26" stroke="#d9dbe2"/>
      <circle cx="110" cy="35" r="26" stroke="#8f93a3" stroke-dasharray="66 164" transform="rotate(-90 110 35)"/>
    </g>
    <g font-family="Montserrat" font-weight="700" font-size="9" fill="#211f52" text-anchor="middle">
      <text x="35" y="38">65%</text><text x="110" y="38">40%</text>
    </g>
  </svg>
  <p class="copy" style="position:absolute;left:170px;top:38px;right:14px">Desktop research, benchmarks and visitor data inform our findings.</p>
</section>

<!-- Consultation -->
<section class="slide consult">
  <h2 class="head">Consultation And Engagement</h2><span class="mark"></span>
  <div style="position:absolute;left:12px;right:12px;top:30px;display:grid;grid-template-columns:repeat(3,1fr);gap:6px">
    <div><div class="photo" style="position:relative;height:56px" role="img" aria-label="Photo of a community workshop"></div><p class="copy" style="margin-top:4px">Workshops</p></div>
    <div><div class="photo" style="position:relative;height:56px" role="img" aria-label="Photo of stakeholder interviews"></div><p class="copy" style="margin-top:4px">Interviews</p></div>
    <div><div class="photo" style="position:relative;height:56px" role="img" aria-label="Photo of people completing a survey"></div><p class="copy" style="margin-top:4px">Surveys</p></div>
  </div>
</section>

<!-- Audits -->
<section class="slide audits">
  <h2 class="head">Relevant Audits</h2><span class="mark"></span>
  <svg style="position:absolute;left:12px;top:42px" width="248" height="30" viewBox="0 0 248 30" aria-hidden="true">
    <line x1="15" y1="15" x2="233" y2="15" stroke="#d9dbe2" stroke-width="2"/>
    <g fill="#211f52"><circle cx="15" cy="15" r="12"/><circle cx="88" cy="15" r="12"/><circle cx="161" cy="15" r="12"/><circle cx="233" cy="15" r="12"/></g>
    <g stroke="#fff" stroke-width="2" fill="none" stroke-linecap="round"><path d="M10 15 l4 4 l7 -8"/><path d="M83 15 l4 4 l7 -8"/><path d="M156 15 l4 4 l7 -8"/><path d="M228 15 l4 4 l7 -8"/></g>
  </svg>
  <div style="position:absolute;left:8px;right:8px;top:82px;display:grid;grid-template-columns:repeat(4,1fr);gap:4px;text-align:center">
    <p class="copy">Asset audit</p><p class="copy">Events audit</p><p class="copy">Tourism audit</p><p class="copy">Policy audit</p>
  </div>
</section>

<!-- Economic -->
<section class="slide economic">
  <h2 class="head">Economic Analysis</h2><span class="mark"></span>
  <svg style="position:absolute;left:12px;top:30px" width="248" height="110" viewBox="0 0 248 110" aria-hidden="true">
    <g stroke="#e3e4ea" stroke-width="1"><line x1="0" y1="20" x2="118" y2="20"/><line x1="0" y1="50" x2="118" y2="50"/><line x1="0" y1="80" x2="118" y2="80"/></g>
    <polyline points="4,78 24,60 44,66 64,40 84,46 104,22" fill="none" stroke="#211f52" stroke-width="2"/>
    <polyline points="4,88 24,80 44,72 64,70 84,58 104,54" fill="none" stroke="#8f93a3" stroke-width="2"/>
    <g fill="#211f52">
      <rect x="136" y="50" width="12" height="50"/><rect x="160" y="34" width="12" height="66"/><rect x="184" y="58" width="12" height="42"/><rect x="208" y="22" width="12" height="78"/>
    </g>
    <g fill="#8f93a3"><rect x="148" y="64" width="8" height="36"/><rect x="172" y="50" width="8" height="50"/><rect x="196" y="70" width="8" height="30"/><rect x="220" y="40" width="8" height="60"/></g>
    <line x1="130" y1="100" x2="240" y2="100" stroke="#8f93a3" stroke-width="1"/>
  </svg>
</section>

<!-- Gap analysis -->
<section class="slide gap">
  <h2 class="head">Gap Analysis</h2><span class="mark"></span>
  <svg style="position:absolute;left:12px;top:32px" width="248" height="100" viewBox="0 0 248 100" aria-hidden="true">
    <g fill="#e3e4ea"><rect x="30" y="4" width="210" height="14" rx="7"/><rect x="30" y="30" width="210" height="14" rx="7"/><rect x="30" y="56" width="210" height="14" rx="7"/><rect x="30" y="82" width="210" height="14" rx="7"/></g>
    <g fill="#211f52"><rect x="30" y="4" width="150" height="14" rx="7"/><rect x="30" y="56" width="120" height="14" rx="7"/></g>
    <g fill="#8f93a3"><rect x="30" y="30" width="180" height="14" rx="7"/><rect x="30" y="82" width="90" height="14" rx="7"/></g>
    <g fill="#211f52"><circle cx="11" cy="11" r="9"/><circle cx="11" cy="63" r="9"/></g>
    <g fill="#8f93a3"><circle cx="11" cy="37" r="9"/><circle cx="11" cy="89" r="9"/></g>
  </svg>
</section>

<!-- SWOT -->
<section class="slide swot">
  <h2 class="head">SWOT</h2><span class="mark"></span>
  <div style="position:absolute;left:90px;top:30px;width:96px;height:96px;display:grid;grid-template-columns:1fr 1fr;gap:4px;font:800 18px 'Montserrat',sans-serif;text-align:center">
    <div style="background:var(--navy);color:#fff;line-height:46px">S</div>
    <div style="background:var(--grey-light);color:var(--navy);line-height:46px">W</div>
    <div style="background:var(--grey-light);color:var(--navy);line-height:46px">O</div>
    <div style="background:var(--navy);color:#fff;line-height:46px">T</div>
  </div>
  <p class="copy" style="position:absolute;left:12px;top:40px;width:70px">Strengths of the region and assets.</p>
  <p class="copy" style="position:absolute;left:12px;top:90px;width:70px">Opportunities for growth.</p>
  <p class="copy" style="position:absolute;left:196px;top:40px;width:64px">Weaknesses to address.</p>
  <p class="copy" style="position:absolute;left:196px;top:90px;width:64px">Threats and risks.</p>
</section>

<!-- Issues -->
<section class="slide issues">
  <h2 class="head">Issues And Opportunities</h2><span class="mark"></span>
  <svg style="position:absolute;left:76px;top:28px" width="120" height="120" viewBox="0 0 120 120" aria-hidden="true">
    <g stroke="#d9dbe2" stroke-width="1.5"><line x1="60" y1="60" x2="60" y2="12"/><line x1="60" y1="60" x2="106" y2="45"/><line x1="60" y1="60" x2="88" y2="100"/><line x1="60" y1="60" x2="32" y2="100"/><line x1="60" y1="60" x2="14" y2="45"/></g>
    <circle cx="60" cy="60" r="22" fill="#211f52"/>
    <g fill="#fff" stroke="#211f52" stroke-width="2"><circle cx="60" cy="12" r="10"/><circle cx="106" cy="45" r="10"/><circle cx="88" cy="100" r="10"/><circle cx="32" cy="100" r="10"/><circle cx="14" cy="45" r="10"/></g>
  </svg>
  <p class="copy" style="position:absolute;left:12px;top:40px;width:60px">Key issues</p>
  <p class="copy" style="position:absolute;left:206px;top:40px;width:56px">Opportunities</p>
</section>

<!-- Case studies -->
<section class="slide cases">
  <h2 class="head">Case Studies And Previous Relevant Work</h2><span class="mark"></span>
  <div style="position:absolute;left:12px;right:12px;top:28px;display:grid;grid-template-columns:repeat(3,1fr);gap:6px">
    <div class="photo" style="position:relative;height:50px" role="img" aria-label="Photo of a sports stadium project"></div>
    <div class="photo" style="position:relative;height:50px" role="img" aria-label="Photo of a tourism destination"></div>
    <div class="photo" style="position:relative;height:50px" role="img" aria-label="Photo of a major event crowd"></div>
    <p class="copy">Regional stadium plan</p><p class="copy">Coastal tourism strategy</p><p class="copy">Festival impact study</p>
  </div>
</section>

<!-- Timeline -->
<section class="slide timeline">
  <h2 class="head">Project Timeline</h2><span class="mark"></span>
  <svg style="position:absolute;left:60px;top:28px" width="200" height="115" viewBox="0 0 200 115" aria-hidden="true">
    <path d="M10 100 C60 100 40 60 100 60 S150 18 190 14" fill="none" stroke="#211f52" stroke-width="3"/>
    <g fill="#211f52"><circle cx="10" cy="100" r="6"/><circle cx="100" cy="60" r="6"/><circle cx="190" cy="14" r="6"/></g>
    <g fill="#8f93a3"><circle cx="56" cy="86" r="4"/><circle cx="148" cy="30" r="4"/></g>
  </svg>
  <div style="position:absolute;left:12px;top:36px;width:60px">
    <p class="sub" style="font-size:7px">FOR 2 YEARS</p>
    <p class="copy" style="margin-top:4px">Stages from inception to final report.</p>
  </div>
</section>

<!-- Budget -->
<section class="slide budget-slide">
  <h2 class="head">Project Budget</h2><span class="mark"></span>
  <table class="budget">
    <tr><th>Stage</th><th>Days</th><th>Fee</th></tr>
    <tr><td>Situation analysis</td><td>12</td><td>$18,000</td></tr>
    <tr><td>Consultation</td><td>8</td><td>$12,000</td></tr>
    <tr><td>Draft report</td><td>6</td><td>$9,000</td></tr>
    <tr><td>Final report</td><td>4</td><td>$6,000</td></tr>
  </table>
</section>

<!-- Thank you -->
<section class="slide dark thanks">
  <div class="photo" style="left:0;top:0;width:100px;height:153px" role="img" aria-label="Photo of a business handshake"></div>
  <div style="position:absolute;left:118px;top:26px">
    <div class="brand"><i></i>VELKOR42</div>
    <p class="big" style="margin-top:20px;font-size:16px">Thank You</p>
    <p class="kicker" style="margin-top:6px;color:#b6b8d0">CONTACT US</p>
    <p class="url" style="margin-top:4px">www.velkor42.com.au</p>
  </div>
</section>

</main>
</body>
</html>
```